Bramwell Construction
Letterhead, Bus Cards, Folders, CDs, note pad
Project: Bramwell Construction
Bramwell Construction -
Creative Brief
Professional
Martin L. Carraway
Chief Thinker
4815 Kellerman Pl N. Seattle, WA 98107
Martin@BramwellBuilds-example.com
http://bramwellbuilds-example.com
Surprise me. May be a watermark with the logo

```html
<!DOCTYPE html>
<html lang="en">
<head>
<meta charset="utf-8">
<title>Bramwell Construction – Stationery</title>
<link href="https://fonts.googleapis.com/css2?family=Arimo:wght@400;700&display=swap" rel="stylesheet">
<style>
:root{
  --bg-edge:#4d4f52;
  --bg-glow:#7a9cbc;
  --band:#1d4a74;
  --brand:#24487a;
  --ink:#3c3f44;
  --paper:#ffffff;
  --swirl-a:#e9edf5;
  --swirl-b:#aab7d3;
  --swirl-c:#6f82ad;
  --mark:#c9cfdc;
}
*{margin:0;padding:0;box-sizing:border-box}
html,body{width:1200px;height:912px;overflow:hidden}
body{font-family:"Arimo",Arial,sans-serif;color:var(--ink);
  background:radial-gradient(ellipse 620px 520px at 430px 400px,var(--bg-glow) 0%,#5f7892 45%,var(--bg-edge) 100%);
  position:relative}
.piece{position:absolute;background:var(--paper);box-shadow:2px 3px 8px rgba(0,0,0,.35)}
.brand{display:flex;align-items:center;gap:6px}
.brand-square{background:var(--brand);flex:none}
.brand-name{font-weight:700;color:var(--brand);letter-spacing:.02em;white-space:nowrap}

/* CD */
.cd{position:absolute;left:12px;top:56px;width:306px;height:306px;border-radius:50%;
  background:radial-gradient(circle at 35% 40%,var(--swirl-a),var(--swirl-b) 55%,var(--swirl-c));
  box-shadow:2px 3px 8px rgba(0,0,0,.35)}
.cd-hole{position:absolute;left:103px;top:103px;width:100px;height:100px;border-radius:50%;background:#fff}
.cd .brand{position:absolute;left:80px;top:70px}
.cd .brand-square{width:10px;height:10px}
.cd .brand-name{font-size:10px}

/* Business card back */
.card-back{left:84px;top:493px;width:236px;height:133px;border-radius:10px;z-index:1;
  background:linear-gradient(120deg,var(--swirl-a),var(--swirl-b) 60%,var(--swirl-c))}
.card-back .brand{position:absolute;left:18px;top:36px}
.card-back .brand-square{width:9px;height:9px}
.card-back .brand-name{font-size:9px}

/* Business card front – sits above the notepad */
.card-front{left:172px;top:655px;width:239px;height:133px;border-radius:8px;z-index:5}
.card-front .brand{position:absolute;left:10px;top:12px;gap:4px}
.card-front .brand-square{width:7px;height:7px}
.card-front .brand-name{font-size:7.5px}
.card-front .person{position:absolute;right:10px;top:10px;font-size:10px;font-weight:700;color:var(--brand);white-space:nowrap}
.card-front .mark{position:absolute;left:88px;top:32px;width:56px;height:56px;border-radius:10px;background:var(--mark);opacity:.4}
.card-front .address{position:absolute;left:10px;top:84px;font-size:6.5px;line-height:1.45;white-space:nowrap}
.card-front .web{position:absolute;right:10px;top:96px;font-size:6.5px;line-height:1.45;text-align:right;white-space:nowrap}

/* Letterhead & notepad */
.sheet-band{height:30px;background:var(--band)}
.sheet .brand{position:absolute}
.sheet .address{position:absolute;text-align:right;line-height:1.4;white-space:nowrap}
.sheet .url{position:absolute;writing-mode:vertical-rl;color:var(--ink);white-space:nowrap}
.letterhead{left:581px;top:59px;width:570px;height:606px;z-index:2}
.letterhead .sheet-band{height:26px}
.letterhead .brand{left:14px;top:50px}
.letterhead .brand-square{width:13px;height:13px}
.letterhead .brand-name{font-size:12px}
.letterhead .tagline{position:absolute;left:33px;top:70px;font-size:8px;color:var(--brand)}
.letterhead .address{right:16px;top:40px;font-size:12px}
.letterhead .url{right:10px;bottom:20px;font-size:9px}

.notepad{left:380px;top:298px;width:391px;height:554px;z-index:3}
.notepad .sheet-band{height:24px}
.notepad .brand{left:12px;top:40px;gap:4px}
.notepad .brand-square{width:8px;height:8px}
.notepad .brand-name{font-size:8.5px}
.notepad .address{right:14px;top:38px;font-size:6.5px}
.notepad .url{right:8px;bottom:18px;font-size:7.5px}
.notepad .watermark{position:absolute;left:84px;top:170px;width:216px;height:216px;border-radius:36px;background:var(--mark);opacity:.35}
.notepad .watermark-name{position:absolute;left:0;right:0;top:402px;text-align:center;font-size:15px;font-weight:700;color:var(--mark);opacity:.8}
</style>
</head>
<body>

<div class="cd" role="img" aria-label="CD label with soft blue swirl artwork">
  <div class="brand"><span class="brand-square"></span><span class="brand-name">BRAMWELL CONSTRUCTION</span></div>
  <div class="cd-hole"></div>
</div>

<div class="piece card-back" role="img" aria-label="Business card back with blue swirl artwork">
  <div class="brand"><span class="brand-square"></span><span class="brand-name">BRAMWELL CONSTRUCTION</span></div>
</div>

<div class="piece sheet letterhead">
  <div class="sheet-band"></div>
  <div class="brand"><span class="brand-square"></span><span class="brand-name">BRAMWELL CONSTRUCTION</span></div>
  <div class="tagline">Built With Purpose</div>
  <div class="address">4815 Kellerman Pl N.<br>Seattle, WA 98107<br>Phone : (206) 555-0147<br>Fax : (206) 555-0182</div>
  <div class="url">http://bramwellbuilds-example.com</div>
</div>

<div class="piece sheet notepad">
  <div class="sheet-band"></div>
  <div class="brand"><span class="brand-square"></span><span class="brand-name">BRAMWELL CONSTRUCTION</span></div>
  <div class="address">4815 Kellerman Pl N.<br>Seattle, WA 98107<br>Phone: (206) 555-0147<br>Fax: (206) 555-0182</div>
  <div class="watermark"></div>
  <div class="watermark-name">BRAMWELL CONSTRUCTION</div>
  <div class="url">http://bramwellbuilds-example.com</div>
</div>

<div class="piece card-front">
  <div class="mark"></div>
  <div class="brand"><span class="brand-square"></span><span class="brand-name">BRAMWELL CONSTRUCTION</span></div>
  <div class="person">Martin L. Carraway</div>
  <div class="address">4815 Kellerman Pl N.<br>Seattle, WA 98107<br>Phone: (206) 555-0147<br>Fax: (206) 555-0182</div>
  <div class="web">Martin@BramwellBuilds-example.com<br>http://bramwellbuilds-example.com</div>
</div>

</body>
</html>
```